Website Design for Hulls for Heroes

Please design and code a new website.
Here are the sites I like best:
http://www.wavelarkit.com/alternate/
http://www.wheelsgivenback.org
Please make it similar. This is NOT a car donation site. It's a boat donation site. I just like this sites above as a lead generation sites.
Old site:
http://hullsforheroes.org
Updates
Coding
Coded - Design and coding required
Number of Pages Required
1 page
Look and feel
Each slider illustrates characteristics of the customer's brand and the style your logo design should communicate.

```html
<!DOCTYPE html>
<html lang="en">
<head>
<meta charset="utf-8">
<title>Hulls for Heroes – Donate Your Boat</title>
<link rel="stylesheet" href="https://fonts.googleapis.com/css2?family=Roboto:wght@400;500;700;900&family=Open+Sans:wght@400;600;700&display=swap">
<style>
:root{
  --navy:#0d2a7a;
  --navy-deep:#0a1c52;
  --blue-band:#25449a;
  --red:#b3181e;
  --red-dark:#8e1015;
  --white:#ffffff;
  --ink:#1c1c1c;
  --muted:#4a4a4a;
  --line:#d4d4d4;
  --gold:#e6c27a;
}
*{box-sizing:border-box;margin:0;padding:0}
html,body{width:1200px;height:2956px;overflow:hidden}
body{font-family:"Open Sans",Arial,sans-serif;color:var(--ink);background:var(--white);position:relative}
section,header,footer{position:absolute;left:0;width:1200px}
.abs{position:absolute}

/* header */
.site-header{top:0;height:158px;background:linear-gradient(100deg,#141a2e 0%,#2a3150 45%,#5a2630 80%,#2a1d2c 100%)}
.brand{left:120px;top:54px;display:flex;align-items:center;gap:16px}
.brand-dot{width:46px;height:46px;border-radius:50%;background:var(--red)}
.brand-name{font-family:"Roboto",sans-serif;font-weight:900;font-size:34px;color:var(--white);letter-spacing:.5px;text-transform:uppercase}
.call{display:flex;align-items:center;gap:14px;color:var(--white);font-family:"Roboto",sans-serif}
.call-icon{width:70px;height:70px;border-radius:50%;border:4px solid var(--white);display:flex;align-items:center;justify-content:center}
.call-kicker{font-weight:700;font-size:22px;line-height:1}
.call-number{font-weight:900;font-size:40px;line-height:1.05}
.call-note{font-weight:700;font-size:15px}
.site-header .call{left:806px;top:22px}

/* nav */
.main-nav{top:158px;left:0;width:804px;height:42px;background:var(--red);display:flex;align-items:center}
.main-nav a{position:absolute;color:var(--white);text-decoration:none;font-family:"Roboto",sans-serif;font-weight:700;font-size:16px;text-transform:uppercase}
.form-head{top:158px;left:804px;width:396px;height:42px;background:var(--white);display:flex;align-items:center;justify-content:center;font-family:"Roboto",sans-serif;font-weight:700;font-size:19px;color:var(--navy)}

/* hero */
.hero-photo{top:200px;left:0;width:804px;height:494px;background:linear-gradient(120deg,#6d7148 0%,#c9c4bb 40%,#eef0f2 65%,#cdd3da 100%)}
.donate-form{top:200px;left:804px;width:396px;height:494px;background:var(--navy)}
.form-title{position:absolute;top:38px;left:0;width:100%;text-align:center;color:var(--white);font-family:"Roboto",sans-serif;font-weight:700;font-size:16px}
.field{position:absolute;height:32px;background:var(--white);border:1px solid #c8cbd6;border-radius:3px;font-size:12px;font-weight:600;color:var(--navy);padding:7px 10px}
.field.select::after{content:"";position:absolute;right:10px;top:12px;border:6px solid transparent;border-top:8px solid var(--navy)}
.col-a{left:20px;width:153px}.col-b{left:185px;width:154px}.col-full{left:20px;width:319px}
.btn-donate{position:absolute;left:20px;top:369px;width:154px;height:40px;background:var(--red);border:1px solid var(--red-dark);color:var(--white);font-family:"Roboto",sans-serif;font-weight:700;font-size:15px;display:flex;align-items:center;justify-content:center}

/* band */
.promo-band{top:694px;height:199px;background:linear-gradient(90deg,#1e3a8e 0%,#2f4fa6 50%,#243f93 100%)}
.promo-badge{left:79px;top:8px}
.promo-text{position:absolute;left:79px;top:30px;width:443px;text-align:center;color:var(--white);font-family:"Roboto",sans-serif;font-weight:900;text-transform:uppercase}
.promo-text .small{font-size:24px;line-height:1.2}
.promo-text .big{font-size:52px;line-height:1.05;color:#f3dada;letter-spacing:2px}
.perk{position:absolute;top:40px;width:140px;text-align:center;color:var(--white);font-family:"Roboto",sans-serif;font-weight:700;font-size:13px;line-height:1.3}
.perk svg{display:block;margin:0 auto 14px}

/* headings */
.section-title{position:absolute;left:0;width:1200px;display:flex;align-items:center;justify-content:center;gap:28px;font-family:"Roboto",sans-serif;font-weight:900;font-size:30px;text-transform:uppercase;color:var(--navy)}
.section-title::before,.section-title::after{content:"";width:120px;height:1px;background:var(--line)}
.section-title em{font-style:normal;color:var(--red)}

/* how */
.how{top:893px;height:368px}
.step{position:absolute;top:160px;font-family:"Roboto",sans-serif}
.step h3{font-weight:700;font-size:15px;color:var(--navy);text-transform:uppercase;line-height:1.25;margin-bottom:10px}
.step p{font-family:"Open Sans",sans-serif;font-weight:600;font-size:13px;line-height:1.45;color:var(--muted)}

/* why */
.why{top:1261px;height:585px;background:linear-gradient(135deg,#2c4496 0%,#3a56a8 45%,#2a3e8a 100%)}
.why .section-title{color:var(--white);top:74px}
.why .section-title::before,.why .section-title::after{background:rgba(255,255,255,.5)}
.reason{position:absolute;width:300px;color:var(--white);font-size:13.5px;line-height:1.35;font-weight:400}
.reason b{font-weight:700}
.reason.left{text-align:left}

/* faq */
.faq{top:1846px;height:617px}
.faq-list{position:absolute;left:83px;top:132px;width:483px}
.faq-item{position:absolute;left:0;width:483px;border:1px solid var(--line);border-radius:12px;background:var(--white);font-family:"Roboto",sans-serif}
.faq-q{height:38px;display:flex;align-items:center;padding:0 16px;font-weight:700;font-size:15px;color:#2b2b2b;justify-content:space-between}
.faq-q::after{content:"";width:7px;height:7px;border-right:2px solid #444;border-bottom:2px solid #444;transform:rotate(45deg);margin-top:-4px}
.faq-item.open .faq-q::after{transform:rotate(-135deg);margin-top:4px}
.faq-a{padding:0 16px;font-family:"Open Sans",sans-serif;font-size:13px;line-height:1.55;color:#444}
.faq-photo{position:absolute;left:601px;top:132px;width:518px;height:414px;background:linear-gradient(180deg,#3a4a66 0%,#a07040 55%,#d9a55a 70%,#2a2320 100%)}

/* footer */
.site-footer{top:2463px;height:449px;background:linear-gradient(110deg,#203a8c 0%,#2a459a 55%,#5a2f52 85%,#3a2a6a 100%)}
.footer-brand{left:0;width:1200px;top:54px;display:flex;justify-content:center;align-items:center;gap:16px}
.footer-col{position:absolute;top:172px;color:var(--white)}
.footer-col h4{font-family:"Roboto",sans-serif;font-weight:700;font-size:14px;text-transform:uppercase;padding-bottom:10px;border-bottom:1px solid rgba(255,255,255,.35);margin-bottom:14px}
.footer-col p{font-size:12px;line-height:1.5;font-weight:600}
.footer-col a{display:block;color:var(--white);text-decoration:none;font-size:12px;font-weight:600;line-height:1.45;text-transform:uppercase}
.badge{display:block;background:rgba(255,255,255,.9);margin-bottom:12px}
.footer-call{position:absolute;left:782px;top:167px;width:347px;height:148px;background:rgba(150,30,45,.75);display:flex;align-items:center;justify-content:center}
.footer-call .call-kicker{font-size:19px}.footer-call .call-number{font-size:33px}.footer-call .call-note{font-size:13px}
.footer-call .call-icon{width:60px;height:60px}
.copyright{position:absolute;top:2912px;left:0;width:1200px;height:44px;background:var(--white);display:flex;align-items:center;justify-content:center;font-family:"Roboto",sans-serif;font-weight:700;font-size:12px;color:#222;text-transform:uppercase}
</style>
</head>
<body>

<header class="site-header">
  <div class="brand abs"><span class="brand-dot"></span><span class="brand-name">Hulls for Heroes</span></div>
  <div class="call abs">
    <span class="call-icon"><svg width="34" height="34" viewBox="0 0 24 24"><path fill="#fff" d="M6.6 10.8a15.1 15.1 0 0 0 6.6 6.6l2.2-2.2c.3-.3.7-.4 1-.2 1.1.4 2.3.6 3.6.6.6 0 1 .4 1 1V20c0 .6-.4 1-1 1C10.6 21 3 13.4 3 4c0-.6.4-1 1-1h3.5c.6 0 1 .4 1 1 0 1.3.2 2.5.6 3.6.1.3 0 .7-.2 1z"/></svg></span>
    <div><div class="call-kicker">CALL TODAY TO DONATE</div><div class="call-number">1-800-555-0142</div><div class="call-note">Live Operators Available - 7 Days A Week</div></div>
  </div>
</header>

<nav class="main-nav abs">
  <a href="#how" style="left:178px">How to Donate</a>
  <a href="#why" style="left:364px">Why Donate</a>
  <a href="#faq" style="left:524px">FAQ</a>
  <a href="#about" style="left:610px">About</a>
</nav>
<div class="form-head abs">DONATE YOUR BOATS ONLINE</div>

<div class="hero-photo abs" role="img" aria-label="Soldier in uniform hugging a child holding a small flag, with a motor yacht and city skyline sketch behind"></div>

<form class="donate-form abs">
  <div class="form-title">Full Tax Deduction - Running or Not</div>
  <div class="field col-a" style="top:70px">First Name</div>
  <div class="field col-b" style="top:70px">Last Name</div>
  <div class="field col-a" style="top:111px">Daytime Phone</div>
  <div class="field col-b" style="top:111px">Email</div>
  <div class="field col-full" style="top:155px">Pickup Address</div>
  <div class="field col-full" style="top:198px">Pickup City</div>
  <div class="field col-a select" style="top:241px">Pickup State</div>
  <div class="field col-b" style="top:241px">Zip Code</div>
  <div class="field col-a select" style="top:285px">Choose Year</div>
  <div class="field col-b select" style="top:285px">Choose Make</div>
  <div class="field col-full" style="top:326px">Vehicle Model</div>
  <div class="btn-donate">DONATE NOW</div>
</form>

<section class="promo-band">
  <svg class="abs promo-badge" width="443" height="183" viewBox="0 0 443 183"><polygon points="40,0 403,0 443,91 403,183 40,183 0,91" fill="#b3181e"/><polygon points="40,0 403,0 443,91 0,91" fill="#c8232a"/></svg>
  <div class="promo-text"><div class="small">Donate your boats to</div><div class="big">Veterans</div><div class="small">Make a difference</div></div>
  <div class="perk" style="left:560px">
    <svg width="58" height="58" viewBox="0 0 58 58"><circle cx="29" cy="29" r="26" fill="none" stroke="#fff" stroke-width="3"/><path d="M17 30l9 9 17-19" fill="none" stroke="#fff" stroke-width="4"/></svg>You have<br>no costs</div>
  <div class="perk" style="left:708px">
    <svg width="58" height="58" viewBox="0 0 58 58"><path d="M6 36h46l-8 10H14z" fill="#fff"/><path d="M18 36v-9h18l8 9" fill="none" stroke="#fff" stroke-width="3"/></svg>Free pickup,<br>running or not</div>
  <div class="perk" style="left:862px">
    <svg width="58" height="58" viewBox="0 0 58 58"><rect x="14" y="5" width="30" height="46" fill="none" stroke="#fff" stroke-width="3"/><path d="M20 16h18M20 24h18M20 32h18M20 40h10" stroke="#fff" stroke-width="2.5"/></svg>We issue you an<br>IRS tax receipt</div>
  <div class="perk" style="left:1000px">
    <svg width="58" height="58" viewBox="0 0 58 58"><rect x="8" y="10" width="30" height="40" fill="none" stroke="#fff" stroke-width="3"/><circle cx="40" cy="24" r="11" fill="#25449a" stroke="#fff" stroke-width="3"/><path d="M14 22h12M14 30h14M14 38h16" stroke="#fff" stroke-width="2.5"/></svg>We take care of<br>all paperwork.</div>
</section>

<section class="how" id="how">
  <h2 class="section-title" style="top:86px">How to <em>Donate</em></h2>
  <svg class="abs" style="left:79px;top:160px" width="68" height="80" viewBox="0 0 68 80"><rect x="0" y="0" width="68" height="12" fill="#0d2a7a"/><rect x="0" y="20" width="68" height="12" fill="#0d2a7a"/><rect x="0" y="40" width="68" height="12" fill="#0d2a7a"/><rect x="20" y="0" width="10" height="52" fill="#fff"/><path d="M10 58l14 14 10-6-6 14z" fill="#0d2a7a"/></svg>
  <div class="step" style="left:161px;width:270px"><h3>Call us at 1-800-555-0142 or<br>fill out the online form</h3><p>Donating your boat is easy and<br>donation is accepted nationwide.</p></div>
  <svg class="abs" style="left:449px;top:170px" width="84" height="46" viewBox="0 0 84 46"><path d="M0 24h84l-12 18H12z" fill="#b3181e"/><path d="M22 24V10h28l12 14" fill="none" stroke="#b3181e" stroke-width="5"/><rect x="30" y="14" width="8" height="6" fill="#b3181e"/></svg>
  <div class="step" style="left:555px;width:280px"><h3>We pick up the boat</h3><p>Any boats is accepted and we will<br>arrange to pick up your boat when<br>it is most convenient for you.</p></div>
  <svg class="abs" style="left:847px;top:160px" width="70" height="84" viewBox="0 0 70 84"><rect x="4" y="4" width="46" height="72" fill="none" stroke="#0d2a7a" stroke-width="4"/><rect x="20" y="12" width="46" height="68" fill="#fff" stroke="#0d2a7a" stroke-width="4"/><text x="43" y="40" font-family="Roboto,sans-serif" font-weight="700" font-size="20" fill="#0d2a7a" text-anchor="middle">$</text><path d="M28 52h30M28 60h30M28 68h20" stroke="#0d2a7a" stroke-width="3"/></svg>
  <div class="step" style="left:942px;width:240px"><h3>Tax write-off</h3><p>Once the boat donation is<br>complete, you will receive your<br>tax deductable boat donation<br>receipt.</p></div>
</section>

<section class="why" id="why">
  <div class="abs" role="img" aria-label="Soldiers and flags in soft focus behind a blue overlay" style="left:0;top:0;width:1200px;height:585px;background:radial-gradient(circle at 60% 55%,rgba(120,110,100,.35),transparent 60%)"></div>
  <h2 class="section-title">Why donate your boats to us</h2>
  <svg class="abs" style="left:0;top:0" width="1200" height="585" viewBox="0 0 1200 585">
    <circle cx="601" cy="295" r="187" fill="#1f2f6a" fill-opacity=".85"/>
    <circle cx="601" cy="295" r="187" fill="none" stroke="#fff" stroke-width="3"/>
    <g stroke="#fff" stroke-width="3">
      <line x1="429" y1="197" x2="478" y2="197"/><line x1="370" y1="335" x2="414" y2="335"/><line x1="429" y1="473" x2="478" y2="473"/>
      <line x1="751" y1="197" x2="722" y2="197"/><line x1="818" y1="335" x2="788" y2="335"/><line x1="759" y1="473" x2="722" y2="473"/>
    </g>
    <g fill="#fff" stroke="#b3181e" stroke-width="3">
      <circle cx="478" cy="197" r="8"/><circle cx="414" cy="335" r="8"/><circle cx="478" cy="473" r="8"/>
      <circle cx="722" cy="197" r="8"/><circle cx="788" cy="335" r="8"/><circle cx="722" cy="473" r="8"/>
    </g>
    <g stroke="#fff" stroke-width="4">
      <circle cx="386" cy="197" r="43" fill="#b3181e"/><circle cx="327" cy="335" r="43" fill="#0d2a7a"/><circle cx="386" cy="473" r="43" fill="#b3181e"/>
      <circle cx="794" cy="197" r="43" fill="#0d2a7a"/><circle cx="861" cy="335" r="43" fill="#b3181e"/><circle cx="802" cy="473" r="43" fill="#0d2a7a"/>
    </g>
    <g fill="none" stroke="#fff" stroke-width="3">
      <path d="M364 204h44l-7 9h-30zM372 204v-10h18l8 10"/>
      <path d="M312 322l30 26M342 322l-30 26"/>
      <path d="M366 465l20-10 20 10-20 10zM366 475l20 10 20-10M366 485l20 10 20-10"/>
      <rect x="780" y="180" width="28" height="34"/>
      <path d="M848 322c0 14 12 26 26 26l4-8-8-4-4 4c-6-3-9-6-12-12l4-4-4-8z" fill="#fff"/>
      <path d="M802 492c-18-12-22-20-18-27 4-6 12-5 18 2 6-7 14-8 18-2 4 7 0 15-18 27z"/>
    </g>
  </svg>
  <div class="reason" style="left:30px;top:190px;width:310px"><b>Free Local Towing :</b> We will pick up your boat donation, running or not, when it's most convenient.</div>
  <div class="reason" style="left:30px;top:318px;width:250px"><b>Income Tax Deduction :</b> We issue you an IRS tax receipt &amp; offer the largest resale network to get you the highest tax write-off possible.</div>
  <div class="reason" style="left:100px;top:458px;width:230px"><b>No Paperwork Hassles :</b> We take any boat and handle everything. DMV, Smog and IRS paperwork.</div>
  <div class="reason" style="left:873px;top:176px;width:300px"><b>Accredited A+ Rated &amp; IRS 501(c)3 Approved :</b> Free 24/7 Pickup with No DMV Hassles.</div>
  <div class="reason" style="left:935px;top:318px;width:245px"><b>Schedule a Free Pickup :</b> Complete the form and a representative will call you to arrange a convenient time to pickup your boat.</div>
  <div class="reason" style="left:873px;top:448px;width:310px"><b>Boat donations help fund programs :</b> And benefit Harbor Heroes Relief Fund. An IRS 501(c)3 nonprofit organization.</div>
</section>

<section class="faq" id="faq">
  <h2 class="section-title" style="top:54px">Frequently asked <em>Questions</em></h2>
  <div class="faq-list">
    <div class="faq-item" style="top:0"><div class="faq-q">What types of boats can be donated?</div></div>
    <div class="faq-item open" style="top:47px;height:138px"><div class="faq-q">What paperwork do I need to donate my boat?</div><p class="faq-a">All you need is a title, free of all liens. We will request some general information from you at the time of donation such as, the year, make, and model of the boat, as well as its general mechanical condition. We accept all boats, running or non-running.</p></div>
    <div class="faq-item" style="top:191px"><div class="faq-q">Is my donated boat tax -deductible?</div></div>
    <div class="faq-item" style="top:240px"><div class="faq-q">What if the boat is not registered in my name?</div></div>
    <div class="faq-item" style="top:287px"><div class="faq-q">How much will I receive as a tax deduction for my boat?</div></div>
    <div class="faq-item" style="top:335px"><div class="faq-q">When will I receive my tax receipt?</div></div>
    <div class="faq-item" style="top:382px"><div class="faq-q">How do I schedule a pick up?</div></div>
  </div>
  <div class="faq-photo" role="img" aria-label="Silhouettes of soldiers raising a flag against a sunset sky"></div>
</section>

<footer class="site-footer" id="about">
  <div class="footer-brand abs"><span class="brand-dot"></span><span class="brand-name">Hulls for Heroes</span></div>
  <div class="footer-col" style="left:73px;width:260px"><h4>About Hulls for Heroes</h4><p>We turn donated boats into lasting support for veterans and their families. Every hull we collect is resold, and the proceeds fund housing, job training and care programs for those who served our nation with honor.</p></div>
  <div class="footer-col" style="left:380px;width:120px"><h4>Navigation</h4><a href="#how">How to Donate</a><a href="#why">Why Donate</a><a href="#faq">FAQ</a><a href="#about">About</a></div>
  <div class="footer-col" style="left:557px;width:160px"><h4>Safe &amp; Secure</h4>
    <span class="badge" style="width:160px;height:50px;border-radius:3px"></span>
    <span class="badge" style="width:110px;height:40px;border-radius:3px"></span>
    <span class="badge" style="width:40px;height:40px;border-radius:50%"></span>
  </div>
  <div class="footer-call call">
    <span class="call-icon"><svg width="30" height="30" viewBox="0 0 24 24"><path fill="#fff" d="M6.6 10.8a15.1 15.1 0 0 0 6.6 6.6l2.2-2.2c.3-.3.7-.4 1-.2 1.1.4 2.3.6 3.6.6.6 0 1 .4 1 1V20c0 .6-.4 1-1 1C10.6 21 3 13.4 3 4c0-.6.4-1 1-1h3.5c.6 0 1 .4 1 1 0 1.3.2 2.5.6 3.6.1.3 0 .7-.2 1z"/></svg></span>
    <div><div class="call-kicker">CALL TODAY TO DONATE</div><div class="call-number">1-800-555-0142</div><div class="call-note">Live Operators Available - 7 Days A Week</div></div>
  </div>
</footer>
<div class="copyright">Copyright © 2017 Hulls for Heroes. Privacy Policy | Terms &amp; Conditions. All rights reserved.</div>

</body>
</html>
```